Corvello Paintless Dent Removal

Our company works on vehicles removing dents using a highly skilled trade which the metal is massaged out with special tools without disturbing the original paint, hence paintless dent removal. Besides keeping the paint and metal original its also very environmentally friendly since no paint or toxic fillers are used. Also we we are one of the most experienced companies in the business with 25 years

Target Market(s)

Retail Automobile consumers, Auto Dealerships and Auto Body Shops

Industry/Entity Type

Auto Repair

Contact Information for Business Card

Dwight Halvorsen
PO Box 538 Ashbrook, NY 11892
631-472-8169
corvellopdr@mailnest.example
website corvellopdr.example
vidora corvello paintless dent removal
25 years of experience removing Dents, Dings and Hail Damage

Font styles to use
Serif
Sans Serif

Colors

Designer to choose colors to be used in the design.

Requirements
Must have
• I do like things that are simple but classy and somewhat bold, also I like my logo so that should be somewhat important

```html
<!DOCTYPE html>
<html lang="en">
<head>
<meta charset="utf-8">
<title>Corvello Paintless Dent Removal — Business Cards</title>
<link rel="stylesheet" href="https://fonts.googleapis.com/css2?family=Work+Sans:wght@400;500;700&display=swap">
<style>
  :root {
    --navy: #13295a;
    --navy-deep: #0e1f47;
    --green: #7cc242;
    --white: #ffffff;
    --backdrop: #4a433d;
  }
  * { box-sizing: border-box; margin: 0; padding: 0; }
  html, body {
    width: 1200px; height: 930px; overflow: hidden;
    background: var(--backdrop);
    font-family: "Work Sans", Arial, sans-serif;
  }
  .sheet {
    width: 1200px; height: 930px;
    display: flex; flex-direction: column; align-items: center; justify-content: center;
    gap: 44px;
  }
  .card {
    position: relative;
    width: 700px; height: 400px;
    border-radius: 18px;
    overflow: hidden;
    box-shadow: 0 6px 18px rgba(0,0,0,.35);
  }
  .card--back {
    background: linear-gradient(135deg, var(--navy) 0%, var(--navy-deep) 100%);
    color: var(--white);
  }
  .wordmark {
    position: absolute; left: 0; right: 0;
    display: flex; align-items: center; justify-content: center; gap: 16px;
    font-weight: 700; color: var(--white);
  }
  .wordmark__dot {
    width: 26px; height: 26px; border-radius: 50%;
    background: var(--green);
    flex: none;
  }
  .wordmark__name { font-size: 34px; letter-spacing: .5px; line-height: 1.15; text-align: left; }
  .wordmark__name small { display: block; font-size: 21px; letter-spacing: .3px; }
  .card--back .wordmark { top: 118px; }
  .tagline {
    position: absolute; left: 0; right: 0; bottom: 64px;
    text-align: center; font-size: 17px; line-height: 1.5;
  }
  .tagline__channel { color: var(--green); font-size: 20px; }

  .card--front { background: var(--white); }
  .front__band {
    position: absolute; left: 0; right: 0; bottom: 0; height: 232px;
    background: linear-gradient(135deg, var(--navy) 0%, var(--navy-deep) 100%);
  }
  .person {
    position: absolute; top: 56px; left: 0; right: 0; text-align: center;
  }
  .person__name {
    font-size: 30px; font-weight: 500; letter-spacing: 1.5px;
    color: var(--navy); text-transform: uppercase;
  }
  .person__role { font-size: 16px; color: var(--green); margin-top: 2px; }
  .card--front .wordmark { top: 196px; }
  .contact {
    position: absolute; left: 0; right: 0; bottom: 42px;
    text-align: center; color: var(--white); font-size: 16.5px; line-height: 1.75;
  }
  .contact__label { color: var(--green); font-weight: 700; }
</style>
</head>
<body>
<main class="sheet">
  <section class="card card--back">
    <div class="wordmark">
      <span class="wordmark__dot"></span>
      <span class="wordmark__name">Corvello<small>Paintless Dent Removal</small></span>
    </div>
    <p class="tagline">
      <span class="tagline__channel">vidora</span> corvello paintless dent removal<br>
      25 years of experience removing Dents, Dings and Hail Damage
    </p>
  </section>

  <section class="card card--front">
    <div class="front__band"></div>
    <div class="person">
      <h1 class="person__name">Dwight Halvorsen</h1>
      <p class="person__role">President</p>
    </div>
    <div class="wordmark">
      <span class="wordmark__dot"></span>
      <span class="wordmark__name">Corvello<small>Paintless Dent Removal</small></span>
    </div>
    <p class="contact">
      <span class="contact__label">P :</span> 631-472-8169 | <span class="contact__label">E :</span> corvellopdr@mailnest.example<br>
      <span class="contact__label">W :</span> www.corvellopdr.example | <span class="contact__label">A :</span> PO Box 538 Ashbrook, NY 11892
    </p>
  </section>
</main>
</body>
</html>
```